We want a hot New Design for our IT company Web Site

We have a basic website with some general information and lots of mostly words and generic pictures we want to make it look and feel a lot more modern and slick. The site needs to work on mobile devices as well as desktops.

Target Market(s)

Business customers

Industry/Entity Type

It Company

Coding

Coded - Design and coding required

Number of Pages Required

5+ page

Requirements
Must have
• Sleek new Design making it look and feel more modern and less boring
Nice to have
• If it can have a better flow to it rather then have the std Drop down menus it has now.

```html
<!DOCTYPE html>
<html lang="en">
<head>
<meta charset="utf-8">
<title>Northvale Solutions Group</title>
<link rel="stylesheet" href="https://fonts.googleapis.com/css2?family=Open+Sans:wght@400;600;700&family=Raleway:wght@500;600;700;800&display=swap">
<style>
  :root{
    --brand:#0e3f85;
    --brand-dark:#0a2d5e;
    --brand-light:#2a7fd4;
    --band-top:#1c6cc4;
    --band-bottom:#0b3a78;
    --ink:#2b2b2b;
    --muted:#777;
    --link:#1d63b5;
    --footer:#3a3a3a;
    --footer-deep:#262626;
    --footer-text:#bdbdbd;
    --white:#fff;
  }
  *{box-sizing:border-box;margin:0;padding:0}
  html,body{width:788px;height:1200px;overflow:hidden}
  body{font-family:"Open Sans",Arial,sans-serif;color:var(--ink);background:var(--white)}
  .page{width:788px;height:1200px;display:flex;flex-direction:column}
  .container{width:700px;margin:0 auto}

  .site-header{height:80px;display:flex;align-items:center}
  .brand{display:flex;align-items:center;gap:10px;font-family:"Raleway",sans-serif;font-weight:800;font-size:17px;color:var(--brand);letter-spacing:.5px}
  .brand-square{width:26px;height:26px;background:var(--brand)}

  .main-nav{height:24px;background:var(--brand)}
  .main-nav ul{list-style:none;display:flex;justify-content:center;gap:42px;height:100%;align-items:center}
  .main-nav a{color:var(--white);text-decoration:none;font-size:9.5px;font-weight:700;letter-spacing:.4px}

  .hero{position:relative;height:316px;background:linear-gradient(120deg,#1d2430 0%,#3b4656 35%,#5c6775 55%,#2a313c 100%);color:var(--white);text-align:center}
  .hero-copy{position:absolute;left:0;right:0;top:190px}
  .hero-title{font-family:"Raleway",sans-serif;font-weight:800;font-size:35px;letter-spacing:.5px;text-shadow:0 2px 6px rgba(0,0,0,.6)}
  .hero-sub{font-family:"Raleway",sans-serif;font-weight:700;font-size:14px;margin-top:2px;letter-spacing:.5px;text-shadow:0 2px 4px rgba(0,0,0,.6)}
  .hero-arrow{position:absolute;top:150px;width:14px;height:24px}
  .hero-arrow.prev{left:14px}
  .hero-arrow.next{right:14px}

  .welcome{height:185px;padding-top:28px;text-align:center}
  .welcome h1{font-family:"Raleway",sans-serif;font-weight:700;font-size:22px;color:var(--ink);margin-bottom:12px}
  .welcome p{font-size:8px;line-height:1.55;color:var(--muted);text-align:left;margin-bottom:8px}

  .services{height:230px;background:linear-gradient(180deg,var(--band-top),var(--band-bottom));padding-top:22px}
  .service-grid{display:flex;justify-content:space-between;width:600px;margin:0 auto}
  .service{width:178px;text-align:center;color:var(--white)}
  .service-media{height:86px;border:3px solid var(--white);background:linear-gradient(135deg,#9fb7d1,#5f7f9f)}
  .service-media.cloud{background:linear-gradient(135deg,#4d6f9c,#1d3660)}
  .service h2{font-family:"Raleway",sans-serif;font-weight:600;font-size:14px;margin:10px 0 5px}
  .service p{font-size:7.5px;line-height:1.5;color:#d8e6f6}
  .btn{display:inline-block;margin-top:10px;background:var(--brand-dark);color:var(--white);font-size:7px;font-weight:700;padding:5px 12px;letter-spacing:.5px}

  .blog{height:185px;padding-top:24px}
  .blog h2.section-title{font-family:"Raleway",sans-serif;font-weight:600;font-size:22px;color:var(--ink);padding-bottom:8px;border-bottom:1px solid #ddd;margin-bottom:14px}
  .posts{display:flex;justify-content:space-between}
  .post{width:200px}
  .post h3{font-family:"Raleway",sans-serif;font-weight:600;font-size:12.5px;color:var(--link);margin-bottom:5px}
  .post p{font-size:7.5px;line-height:1.55;color:var(--muted)}
  .post .more{display:block;font-size:7.5px;font-weight:700;color:var(--ink);margin-top:5px}

  .site-footer{height:152px;background:var(--footer);padding-top:26px;color:var(--footer-text)}
  .footer-cols{display:flex;gap:62px}
  .footer-col h4{font-family:"Raleway",sans-serif;font-size:11px;font-weight:600;color:var(--white);margin-bottom:8px}
  .footer-col li{list-style:none;font-size:7.5px;line-height:1.75}
  .social{display:flex;gap:8px;margin-top:6px}
  .social span{width:12px;height:12px;border-radius:50%;background:var(--white);opacity:.85}
  .copyright{height:28px;background:var(--footer-deep);color:#999;font-size:7px;display:flex;align-items:center}
</style>
</head>
<body>
<div class="page">
  <header class="site-header">
    <div class="container">
      <div class="brand"><span class="brand-square"></span>NORTHVALE SOLUTIONS GROUP</div>
    </div>
  </header>

  <nav class="main-nav">
    <ul>
      <li><a href="#">HOME</a></li>
      <li><a href="#">ABOUT US</a></li>
      <li><a href="#">SERVICES</a></li>
      <li><a href="#">BLOG</a></li>
      <li><a href="#">SUPPORT</a></li>
      <li><a href="#">NEWS</a></li>
      <li><a href="#">CONTACT</a></li>
    </ul>
  </nav>

  <section class="hero" role="img" aria-label="Two business people shaking hands in a server room">
    <svg class="hero-arrow prev" viewBox="0 0 14 24"><path d="M12 2 2 12l10 10" fill="none" stroke="#fff" stroke-width="2.5"/></svg>
    <svg class="hero-arrow next" viewBox="0 0 14 24"><path d="M2 2l10 10L2 22" fill="none" stroke="#fff" stroke-width="2.5"/></svg>
    <div class="hero-copy">
      <div class="hero-title">MANAGED IT SERVICES &amp; HOSTING</div>
      <div class="hero-sub">PRAESENT AMET EST DICTUM DOLOR DICTUM</div>
    </div>
  </section>

  <section class="welcome">
    <div class="container">
      <h1>WELCOME TO NORTHVALE SOLUTIONS GROUP</h1>
      <p>Northvale Solutions Group offers technology consulting, managed IT services and a modern cloud platform for small and mid-sized businesses. Our team keeps your systems secure, your data protected and your people productive, so you can focus on growing the business.</p>
      <p>From network design and helpdesk support to server hosting and backup, we build long-term partnerships with clear pricing, fast response times and friendly engineers who explain things in plain language. Talk to us about a free review of your current setup.</p>
    </div>
  </section>

  <section class="services">
    <div class="service-grid">
      <article class="service">
        <div class="service-media" role="img" aria-label="Consultant working at a desk with a laptop"></div>
        <h2>Technology Consulting</h2>
        <p>Plan your next step with expert advice on infrastructure, security and software that fits the way your team works.</p>
        <span class="btn">READ MORE</span>
      </article>
      <article class="service">
        <div class="service-media" role="img" aria-label="Support team at computer workstations"></div>
        <h2>Managed IT Services</h2>
        <p>Proactive monitoring, patching and support keep every device running smoothly, with one fixed monthly fee and no surprises.</p>
        <span class="btn">READ MORE</span>
      </article>
      <article class="service">
        <div class="service-media cloud" role="img" aria-label="Cloud computing network concept"></div>
        <h2>Cloud &amp; Hosting</h2>
        <p>Host servers, email and files in secure data centres with daily backups and room to grow whenever you need.</p>
        <span class="btn">READ MORE</span>
      </article>
    </div>
  </section>

  <section class="blog">
    <div class="container">
      <h2 class="section-title">Recent Blog Post</h2>
      <div class="posts">
        <article class="post">
          <h3>Cras a ante vitae enim iaculis</h3>
          <p>Simple steps every office can take this month to reduce the risk of phishing and lost data.</p>
          <span class="more">Read More</span>
        </article>
        <article class="post">
          <h3>Mauris vel lacus vitae felis</h3>
          <p>Why moving file storage to the cloud saves time, cuts hardware costs and helps remote staff.</p>
          <span class="more">Read More</span>
        </article>
        <article class="post">
          <h3>Sed metus turpis convallis</h3>
          <p>A quick checklist for planning network upgrades without disrupting your daily operations.</p>
          <span class="more">Read More</span>
        </article>
      </div>
    </div>
  </section>

  <footer class="site-footer">
    <div class="container footer-cols">
      <div class="footer-col">
        <h4>Company</h4>
        <ul><li>About Us</li><li>Our Team</li><li>Careers</li><li>Partners</li></ul>
      </div>
      <div class="footer-col">
        <h4>Our Services</h4>
        <ul><li>Consulting</li><li>Managed IT</li><li>Cloud Hosting</li><li>Backup</li></ul>
      </div>
      <div class="footer-col">
        <h4>Support</h4>
        <ul><li>Help Desk</li><li>Remote Support</li><li>Status</li><li>Contact</li></ul>
      </div>
      <div class="footer-col">
        <h4>Contact Us</h4>
        <ul><li>14 Harbour Lane, Suite 200, Brookfield</li><li>Phone: (555) 014-2280</li><li>hello@northvale.example</li></ul>
        <div class="social"><span></span><span></span><span></span></div>
      </div>
    </div>
  </footer>
  <div class="copyright"><div class="container">© 2024 Northvale Solutions Group. All rights reserved.</div></div>
</div>
</body>
</html>
```